Informative commercial website for a BJJ (brazilian Jiu jitsu) academy

For our academy: Corvan Tessa Groningen we need a new design.
We use the website to attract new people. It should be a SEO friendly design (enough room for keyword rich text). But more important really userfriendly.
Conversion is also a goal: people filling in the trial class form, contact form or subscribe to the newsletter.

Our current (old) website: www.corvantessagroningen.example
You can use the content of this website for the new design.

Example other BJJ academy websites:
www.corvantessa.example
lumekwrestle.example
http://dorianpelkwjj.example/dpa/
http://velmoragrapple.example/

Target Market(s)

BJJ practitioners or people interested in training BJJ

Industry/Entity Type

Commercial

Number of Pages Required

5+ page

Font styles to use
Sans Serif

Requirements
Must have
• Requirements:
• - modern design (material design inspired, flat): https://www.quorbix.example/design/
• - it must be pursuasive for new clients (call to actions, think good about a commercial clickflow, usecase)
• Main page:
• - latest blog posts
• - sign up free trail class
• - pictures
• - benefits of signing up (5 classes per week, all levels, dedicated competition team, continued support: black belt headcoach, international association)
• - link to facebook, youtube, instagram
• - link to our sponsors: www.matworkrolla.example (Shop online store: buy your BJJ gear) and www.cleanshieldo.example
• - Gym address and emailaddress
• - newsletter sign up
• - get started: free class
• Benefits, show with icons:
• - World class instruction
• (competition proven techniques)
• - Structured Corvan Tessa Curriculum
• - Regular special events with top competitors
• - Friendly and challenging environment
• - Will benefit your health and confidence
• Subpages:
• BJJ
• - what is BJJ
• - history of BJJ
• News/Blog
• Corvan Tessa
• - instructors/ colored belts
• - results
• (with sorting options: overall, per year)
• - Etiquette
• - friends (CT Hamburg, CT Sevilla, KTRFL)
• Schedule/ programs
• - Advanced Program
• - Introductory class
• - Competition class
• Contact
• - location/ route
• Use:
• CTG logo
• ct pictures (https://www.pagebook.example/CorvanTessaGroningen)

```html
<!DOCTYPE html>
<html lang="nl">
<head>
<meta charset="utf-8">
<title>Corvan Tessa Groningen</title>
<link href="https://fonts.googleapis.com/css2?family=Open+Sans:wght@400;600;700&family=Roboto+Condensed:wght@400;700&display=swap" rel="stylesheet">
<style>
:root{
  --red:#b3141b;
  --red-dark:#8a0f14;
  --red-deep:#6e0b0f;
  --ink:#2b2b2b;
  --muted:#6b6b6b;
  --line:#dcdcdc;
  --paper:#ffffff;
  --soft:#f1f1f1;
  --blue:#2f7fc4;
  --photo-a:#4a4f5a;
  --photo-b:#8c8f95;
}
*{box-sizing:border-box;margin:0;padding:0}
html,body{width:690px;height:1200px;overflow:hidden;background:var(--paper)}
body{font-family:"Open Sans",sans-serif;color:var(--ink);font-size:8px;position:relative}
.head-font{font-family:"Roboto Condensed",sans-serif}
.wrap{width:620px;margin:0 auto;position:relative}

.topbar{height:14px;background:var(--red-deep);color:#fff;font-size:6.5px}
.topbar .wrap{display:flex;justify-content:space-between;align-items:center;height:14px}
.topbar .right{display:flex;gap:4px;align-items:center}
.sq{width:9px;height:9px;background:var(--red);display:inline-block}
.topbar .cta{background:#fff;color:var(--red);padding:1px 5px;font-weight:700}

.nav{height:56px;background:#fff;border-bottom:2px solid var(--red)}
.nav .wrap{display:flex;align-items:center;justify-content:space-between;height:56px}
.nav ul{display:flex;list-style:none;gap:4px}
.nav li{background:var(--red);color:#fff;font-size:8px;font-weight:600;padding:5px 8px}
.brand{position:absolute;left:50%;top:2px;transform:translateX(-50%);width:96px;height:76px;background:var(--red);color:#fff;display:flex;flex-direction:column;align-items:center;justify-content:center;gap:4px;z-index:3;font-family:"Roboto Condensed",sans-serif;font-weight:700;font-size:10px;text-align:center;line-height:1.1}
.brand i{width:18px;height:18px;border-radius:50%;background:#fff;display:block}

.hero{height:255px;background:linear-gradient(160deg,var(--photo-b),var(--photo-a));position:relative}
.hero .caption{position:absolute;left:35px;top:180px;background:var(--red-dark);color:#fff;font-family:"Roboto Condensed",sans-serif;font-weight:700;font-size:17px;line-height:1.25;padding:6px 12px}
.arrow{position:absolute;top:50%;width:16px;height:24px;margin-top:-12px;background:rgba(0,0,0,.45);color:#fff;font-size:12px;display:flex;align-items:center;justify-content:center}

.welcome{padding:18px 0 0;height:240px}
.welcome .wrap{display:flex;gap:26px}
.welcome .text{flex:1}
h2{font-family:"Roboto Condensed",sans-serif;font-size:16px;font-weight:700;margin-bottom:8px}
h2 span{color:var(--red)}
.welcome p{font-size:7.5px;line-height:1.6;color:var(--muted);margin-bottom:8px}
.btn{display:inline-block;background:var(--red);color:#fff;font-size:7px;font-weight:700;padding:5px 10px}
.benefits{width:220px;background:var(--soft);padding:12px;display:grid;grid-template-columns:1fr 1fr;gap:10px}
.benefit{display:flex;flex-direction:column;align-items:center;text-align:center;font-size:6.5px;font-weight:600;gap:4px}
.benefit .ic{width:42px;height:42px;background:var(--red);border-radius:6px;display:flex;align-items:center;justify-content:center}

.gallery{height:220px;background:var(--soft);text-align:center;padding-top:14px}
.gallery .sub{color:var(--muted);font-size:7px;margin:-4px 0 14px}
.thumbs{display:flex;gap:10px;justify-content:center;position:relative}
.thumb{width:108px;height:80px;background:linear-gradient(150deg,var(--photo-b),var(--photo-a));border:3px solid #fff}
.gallery .arrow{background:none;color:var(--muted);top:40px;margin-top:0}
.dots{margin-top:12px;display:flex;gap:4px;justify-content:center}
.dots i{width:5px;height:5px;border-radius:50%;background:#bbb}
.dots i:first-child{background:var(--red)}

.cols{height:225px;padding-top:14px}
.cols .wrap{display:flex;gap:22px}
.col{flex:1}
.col h3{font-family:"Roboto Condensed",sans-serif;font-size:14px;font-weight:700;margin-bottom:8px;border-bottom:1px solid var(--line);padding-bottom:4px}
.col h3 span{color:var(--red)}
.quote{font-style:italic;color:var(--muted);font-size:6.5px;line-height:1.55;margin-bottom:4px}
.who{color:var(--red);font-size:6.5px;font-weight:600;margin-bottom:10px}
.more{color:var(--red);font-size:7px;font-weight:700}
.col p{color:var(--muted);font-size:6.5px;line-height:1.55;margin-bottom:6px}
.field{height:16px;border:1px solid var(--line);background:#fff;font-size:6.5px;color:#999;padding:3px 5px;margin-bottom:5px}
.btn-blue{background:var(--blue);color:#fff;font-size:7px;font-weight:700;padding:5px 12px;display:inline-block}
.follow{display:flex;align-items:center;gap:5px;margin-top:16px;border-top:1px solid var(--line);padding-top:8px}
.follow b{font-family:"Roboto Condensed",sans-serif;font-size:13px;margin-right:4px}
.follow i{width:16px;height:16px;display:block}
.trial{background:var(--red-dark);padding:10px;color:#fff}
.trial h3{color:#fff;border-color:rgba(255,255,255,.3)}
.trial .row{display:flex;gap:5px}
.trial .row .field{flex:1}
.trial .area{height:28px}
.trial .go{background:var(--red);border:1px solid #fff;color:#fff;font-size:7px;font-weight:700;padding:5px 10px;display:inline-block}

.sponsors{height:70px;border-top:1px solid var(--line)}
.sponsors .wrap{display:flex;align-items:center;height:70px;gap:30px}
.sponsors h3{font-family:"Roboto Condensed",sans-serif;font-size:15px;font-weight:700}
.sponsors h3 span{color:var(--red)}
.sponsor{font-family:"Roboto Condensed",sans-serif;font-weight:700;font-size:16px;color:#555}

.footer{position:absolute;left:0;right:0;bottom:0;height:74px;background:var(--red)}
.footer .links{height:44px;display:flex;justify-content:center;align-items:center;gap:16px;color:#fff;font-size:7px}
.footer .bottom{height:30px;background:var(--red-deep);color:#f0c9cb;font-size:6.5px}
.footer .bottom .wrap{display:flex;justify-content:space-between;align-items:center;height:30px}
</style>
</head>
<body>
<header>
  <div class="topbar"><div class="wrap">
    <span>info@corvantessagroningen.example</span>
    <span class="right"><i class="sq"></i><i class="sq"></i><i class="sq"></i><span class="cta">Sign up for a FREE CLASS</span></span>
  </div></div>
  <nav class="nav"><div class="wrap">
    <ul><li>Braziliaan Jiu-Jitsu</li><li>Nieuws/Blog</li></ul>
    <div class="brand"><i></i>Corvan Tessa<br>Groningen</div>
    <ul><li>Overall</li><li>Schedule &amp; programs</li><li>Contact us</li></ul>
  </div></nav>
</header>

<section class="hero" role="img" aria-label="Group photo of academy members in kimonos on the mats">
  <span class="arrow" style="left:10px">&#8249;</span>
  <span class="arrow" style="right:10px">&#8250;</span>
  <div class="caption">De nieuwe BJJ blue belts van<br>Corvan Tessa Groningen</div>
</section>

<section class="welcome"><div class="wrap">
  <div class="text">
    <h2>Welcome to <span>Corvan Tessa Groningen</span></h2>
    <p>Lorem Ipsum is simply dummy text of the printing and typesetting industry. Lorem Ipsum has been the industry's standard dummy text ever since the 1500s, when an unknown printer took a galley of type and scrambled it to make a type specimen book. It has survived not only five centuries, but also the leap into electronic typesetting, remaining essentially unchanged.</p>
    <p>It was popularised in the 1960s with the release of Letraset sheets containing Lorem Ipsum passages, and more recently with desktop publishing software like Aldus PageMaker including versions of Lorem Ipsum.</p>
    <span class="btn">Read More »</span>
  </div>
  <div class="benefits">
    <div class="benefit"><span class="ic"><svg width="22" height="22" viewBox="0 0 24 24" fill="none" stroke="#fff" stroke-width="2"><path d="M12 2l3 6 7 1-5 5 1 7-6-3-6 3 1-7-5-5 7-1z"/></svg></span>World Class Instruction</div>
    <div class="benefit"><span class="ic"><svg width="22" height="22" viewBox="0 0 24 24" fill="none" stroke="#fff" stroke-width="2"><rect x="3" y="5" width="18" height="16"/><path d="M3 10h18M8 2v6M16 2v6"/></svg></span>Special Events With Top Competitors</div>
    <div class="benefit"><span class="ic"><svg width="22" height="22" viewBox="0 0 24 24" fill="none" stroke="#fff" stroke-width="2"><path d="M4 12l5 5L20 6"/></svg></span>Competition Proven Techniques</div>
    <div class="benefit"><span class="ic"><svg width="22" height="22" viewBox="0 0 24 24" fill="none" stroke="#fff" stroke-width="2"><circle cx="8" cy="8" r="3"/><circle cx="16" cy="8" r="3"/><path d="M2 20c0-4 3-6 6-6s6 2 6 6M12 20c0-4 2-6 4-6s6 2 6 6"/></svg></span>Friendly &amp; Challenging Environment</div>
  </div>
</div></section>

<section class="gallery">
  <h2>Event <span>Gallery</span></h2>
  <p class="sub">Simply dummy text of the printing and typesetting industry.</p>
  <div class="wrap">
    <div class="thumbs">
      <div class="thumb" role="img" aria-label="Event photo of training session"></div>
      <div class="thumb" role="img" aria-label="Event photo of team at competition"></div>
      <div class="thumb" role="img" aria-label="Event photo of seminar"></div>
      <div class="thumb" role="img" aria-label="Event photo of sparring"></div>
      <div class="thumb" role="img" aria-label="Event photo of belt promotion"></div>
    </div>
    <span class="arrow" style="left:-22px">&#8249;</span>
    <span class="arrow" style="right:-22px">&#8250;</span>
  </div>
  <div class="dots"><i></i><i></i><i></i></div>
</section>

<section class="cols"><div class="wrap">
  <div class="col">
    <h3>What <span>People say</span></h3>
    <p class="quote">" It is a long established fact that a reader will be distracted by the readable content of a page when looking at its layout. The point of using Lorem Ipsum is that it has a more-or-less normal distribution of letters."</p>
    <p class="who">Klaas Mulder</p>
    <p class="quote">" It is a long established fact that a reader will be distracted by the readable content of a page when looking at its layout and its distribution of letters."</p>
    <p class="who">Simon Dekker</p>
    <span class="more">See More »</span>
  </div>
  <div class="col">
    <h3>Join <span>Our Newsletter</span></h3>
    <p>Want to keep up to date with all our latest news and information? Enter your email below to be added to our mailing list.</p>
    <div class="field">Enter Email Address</div>
    <span class="btn-blue">Sign Up</span>
    <div class="follow"><b>Follow us</b><i style="background:#3b5998"></i><i style="background:#c1355e"></i><i style="background:#d62c23"></i></div>
  </div>
  <div class="col trial">
    <h3>Try <span style="color:#fff">a Free Class</span></h3>
    <div class="field">Name</div>
    <div class="field">Email</div>
    <div class="field">Phone</div>
    <div class="row"><div class="field">ZIP Code</div><div class="field">Gender</div></div>
    <div class="field area">Tell us Your Goals</div>
    <span class="go">Get My Free Class</span>
  </div>
</div></section>

<section class="sponsors"><div class="wrap">
  <h3>Our <span>Sponsors</span></h3>
  <span class="sponsor">Cleanshieldo</span>
  <span class="sponsor">Matworkrolla</span>
  <span class="sponsor">Nimbrawl</span>
</div></section>

<footer class="footer">
  <div class="links"><span>Home</span><span>Braziliaan Jiu-Jitsu</span><span>Nieuws/Blog</span><span>Corvan Tessa</span><span>Overall</span><span>Schedule &amp; programs</span><span>Contact</span></div>
  <div class="bottom"><div class="wrap">
    <span>© 2015 Corvan Tessa Groningen. All Rights Reserved</span>
    <span>Terms and Conditions | Privacy Policy</span>
  </div></div>
</footer>
</body>
</html>
```